Wordpress Design Project (Bramblewick)

We need a wordpress design for an established auction and real estate company based in New Hampshire. The winning design will incorporate the colors of logo (red and blue) creatively with black or gray in a very professional and clean layout. Client mentions liking the site http://www.veltranbids.com/ as a general idea.

Industry/Entity Type

Real Estate

Requirements
Must have
• Navigation:
1) Home (lorem text)
2) Upcoming Auctions
3) Auction Results
4) Sell or Consign
5) About Us
6) Services
7) FAQ
8) Contact Us

Site will have slideshow, initial image attached.
Sidebar widgets:
- Email sign up form
- Featured Auction (like at http://www.dorvexsalehouse.com) - - - - Video Widget
- Testimonials widget

Footer will have smaller logo, contact info, and 2 association logos (attached)
-
Nice to have
• use of drop-down menu design for 'Services'
1) Appraisals
2) Consulting
Should not have
• please use no gavels in the design

```html
<!DOCTYPE html>
<html lang="en">
<head>
<meta charset="utf-8">
<title>Bramblewick Auctions</title>
<link rel="stylesheet" href="https://fonts.googleapis.com/css2?family=Arimo:ital,wght@0,400;0,700;1,400;1,700&family=Lustria&display=swap">
<style>
:root{
  --navy:#0d1a5a;
  --navy-dark:#08113f;
  --red:#9b1a16;
  --red-deep:#7e1410;
  --ink:#333;
  --ink-soft:#4a4a4a;
  --rule:#d5d5d5;
  --footer:#1d1d1d;
  --white:#fff;
}
*{box-sizing:border-box;margin:0;padding:0}
html,body{width:1200px;height:1190px;overflow:hidden}
body{
  position:relative;
  font-family:"Arimo",Arial,sans-serif;
  color:var(--ink);
  background:linear-gradient(#3a3a3a 0,#8c8c8c 250px,#e9e9e9 440px,#fff 540px,#fff 100%);
}
.abs{position:absolute}
.serif{font-family:"Lustria",Georgia,serif;font-weight:400}

/* header */
.hero-frame{left:102px;top:14px;width:996px;height:466px;background:var(--white);box-shadow:0 0 6px rgba(0,0,0,.25)}
.hero-photo{left:109px;top:21px;width:983px;height:407px;
  background:linear-gradient(160deg,#5b3a2b 0%,#8d6a55 25%,#b7a08a 45%,#7e5b46 70%,#3e2a22 100%)}
.brand-band{left:90px;top:161px;width:1020px;height:110px;
  background:linear-gradient(#ffffffee,#eef0f3ee);box-shadow:0 2px 6px rgba(0,0,0,.3)}
.band-tip{top:150px;width:0;height:0;border-bottom:11px solid var(--red)}
.band-tip.left{left:90px;border-left:12px solid transparent}
.band-tip.right{left:1098px;border-right:12px solid transparent}
.brand{left:130px;top:172px;display:flex;align-items:center;gap:10px}
.brand-mark{width:80px;height:80px;border-radius:50%;background:var(--navy)}
.brand-name{font-family:"Lustria",Georgia,serif;font-size:26px;color:var(--navy);letter-spacing:.5px;margin-top:10px}

/* nav */
.main-nav{left:108px;top:430px;width:984px;height:44px;background:linear-gradient(var(--navy),var(--navy-dark));display:flex}
.main-nav a{color:var(--white);text-decoration:none;font-size:14.5px;letter-spacing:.3px;
  display:flex;align-items:center;justify-content:center;border-right:1px solid #27357a;position:relative}
.main-nav a:last-child{border-right:0}
.nav-caret{position:absolute;left:50%;bottom:3px;margin-left:-5px;border:5px solid transparent;border-top:6px solid var(--white);border-bottom:0}
.dropdown{left:795px;top:475px;width:112px;height:60px;background:var(--red);border-radius:0 0 4px 4px;padding:4px 6px}
.dropdown a{display:block;color:var(--white);font-size:12px;font-weight:700;text-decoration:none;padding:5px 6px;height:27px}
.dropdown a+a{border-top:1px dashed #c9605a}

/* welcome */
.welcome-title{left:110px;top:519px;font-size:24px;color:var(--red);letter-spacing:.3px}
.welcome-title span{color:var(--navy)}
.welcome-copy{left:113px;top:564px;width:668px;font-size:13px;line-height:19px;letter-spacing:.42px;color:var(--ink-soft)}
.welcome-copy p+p{margin-top:19px}
.more-link{left:697px;top:761px;font-size:11px;font-style:italic;color:var(--red);text-decoration:none}
.col-rule{left:815px;top:540px;width:1px;height:236px;background:var(--rule)}

/* featured */
.featured{left:838px;top:522px;width:230px;text-align:center}
.featured h2{font-size:24px;color:#222}
.featured .lot{margin-top:17px;font-size:12px;font-weight:700;color:var(--red)}
.featured .lot-photo{margin:9px auto 0;width:169px;height:114px;border:3px solid #444;
  background:linear-gradient(#a9b3b8 0%,#d8dcde 40%,#596b3e 75%,#3e4a2c 100%)}
.featured .meta{margin-top:8px;font-size:13px;line-height:17px;color:#222;letter-spacing:.2px}

/* testimonials */
.testimonials{left:109px;top:807px;width:290px;height:234px;border:1px solid #dcdcdc;border-radius:5px;
  background:linear-gradient(#fff,#ececec)}
.testimonials h2{position:absolute;left:19px;top:9px;font-size:24px;color:#222}
.quote{position:absolute;left:28px;top:50px;width:248px;font-size:13px;line-height:20px;letter-spacing:.25px;color:#333}
.quote-mark{font-family:"Lustria",Georgia,serif;font-size:32px;color:#999;line-height:10px;vertical-align:-10px}
.author{position:absolute;right:18px;top:207px;font-size:12px;font-weight:700;font-style:italic;color:var(--red-deep)}

/* video */
.video{left:421px;top:812px;width:371px;height:227px;
  background:linear-gradient(120deg,#5a1410 0%,#8c2a20 45%,#b59a6a 55%,#2b2b2b 100%)}
.play{position:absolute;left:140px;top:65px;width:84px;height:59px;border-radius:6px;background:rgba(20,20,20,.85)}
.play::after{content:"";position:absolute;left:31px;top:14px;border-left:28px solid #fff;border-top:15px solid transparent;border-bottom:15px solid transparent}
.controls{position:absolute;left:8px;bottom:2px;width:358px;height:25px;background:#f2f2f2;border:1px solid #bbb;
  display:flex;align-items:center;font-size:11px;color:#111;gap:8px;padding:0 6px}
.controls .track{flex:1;height:5px;background:#c8c8c8;border-radius:2px}

/* signup */
.signup{left:807px;top:811px;width:290px;height:230px;border-radius:6px;border:1px solid #111;
  background:linear-gradient(#4b4b4b,#111 55%,#000)}
.signup h2{position:absolute;left:28px;top:11px;font-size:24px;color:var(--white)}
.signup input{position:absolute;left:29px;width:232px;height:35px;border:0;padding:0 11px;font-family:"Arimo",Arial,sans-serif;font-size:12px;color:#999;background:#fff}
.signup .btn{position:absolute;left:141px;top:172px;width:120px;height:34px;border-radius:4px;border:0;
  background:linear-gradient(#b82a20,var(--red-deep));color:#fff;font-family:"Lustria",Georgia,serif;font-size:18px;letter-spacing:1px}

/* footer */
.site-footer{left:0;top:1094px;width:1200px;height:96px;background:var(--footer)}
.contact{position:absolute;left:108px;top:25px;font-size:12.5px;line-height:23px;color:#eee}
.contact b{color:#fff}
.foot-brand{position:absolute;left:662px;top:26px;width:143px;height:48px;background:#111;border:1px solid #2e2e2e;
  display:flex;align-items:center;justify-content:center;gap:7px}
.foot-brand i{width:28px;height:28px;border-radius:50%;background:#ddd;display:block}
.foot-brand span{font-family:"Lustria",Georgia,serif;font-size:13px;color:#eee}
.badge-a{position:absolute;left:830px;top:28px;width:52px;height:46px;background:#555;border:1px solid #888}
.badge-b{position:absolute;left:919px;top:28px;width:170px;height:42px;background:#f2f2f2}
</style>
</head>
<body>

<header>
  <div class="abs hero-frame"></div>
  <div class="abs hero-photo" role="img" aria-label="Slideshow photo of a display case filled with silver and gold coins in protective holders"></div>
  <div class="abs band-tip left"></div>
  <div class="abs band-tip right"></div>
  <div class="abs brand-band"></div>
  <div class="abs brand"><div class="brand-mark"></div><div class="brand-name">BRAMBLEWICK</div></div>

  <nav class="abs main-nav">
    <a href="#" style="width:86px">Home</a>
    <a href="#" style="width:180px">Upcoming Auctions</a>
    <a href="#" style="width:154px">Auction Results</a>
    <a href="#" style="width:151px">Sell or Consign</a>
    <a href="#" style="width:109px">About Us</a>
    <a href="#" style="width:105px">Services<span class="nav-caret"></span></a>
    <a href="#" style="width:75px">FAQ</a>
    <a href="#" style="width:124px">Contact Us</a>
  </nav>
  <div class="abs dropdown"><a href="#">Appraisals</a><a href="#">Consulting</a></div>
</header>

<main>
  <h1 class="abs welcome-title serif">WELCOME TO <span>BRAMBLEWICK</span></h1>
  <div class="abs welcome-copy">
    <p>When an unknown printer took a galley of type and scrambled it to make a type specimen book. It has survived not only five centuries, but also the leap into electronic typesetting, remaining essentially unchanged. It was popularised in the 1960s with the release of Typoline sheets containing Lorem Ipsum passages. and more recently with desktop publishing software like Folioset Layout including versions of Lorem Ipsum.</p>
    <p>when an unknown printer took a galley of type and scrambled it to make a type specimen book. It has survived not only five centuries, but also the leap into electronic typesetting, remaining essentially unchanged. It was popularised in the 1960s with the release of Typoline sheets containing Lorem Ipsum passages. and more recently.</p>
  </div>
  <a class="abs more-link" href="#">More Details &raquo;</a>
  <div class="abs col-rule"></div>

  <section class="abs featured">
    <h2 class="serif">Featured Auction</h2>
    <div class="lot">AUTOMOBILES - MULTI LOT</div>
    <div class="lot-photo" role="img" aria-label="Photo of a silver minivan parked on grass"></div>
    <div class="meta">07/10/13 at 12:00 PM EDT<br>P.O. Box 4410<br>Hollis Creek, VA 24099</div>
  </section>

  <section class="abs testimonials">
    <h2 class="serif">Testimonials</h2>
    <p class="quote"><span class="quote-mark">&ldquo;</span> simply dummy text of the printing and typesetting industry. Lorem Ipsum has been the industry's took a galley of type and scrambledstandard dummy text ever since the 1500s, when an unknown printer took a galley of type and scrambled it to <span class="quote-mark">&rdquo;</span></p>
    <div class="author">By Mara Thelwell...</div>
  </section>

  <section class="abs video" role="img" aria-label="Video still of a man in a suit beside a large gold coin">
    <div class="play"></div>
    <div class="controls"><span>&#9654;</span><span>00:00</span><span class="track"></span><span>00:00</span><span>&#9646;&#9646;&#9646;</span><span>&#10530;</span></div>
  </section>

  <section class="abs signup">
    <h2 class="serif">Email sign up</h2>
    <input type="text" style="top:59px" placeholder="Enter Your Name">
    <input type="text" style="top:111px" placeholder="Enter Your Email Address...">
    <button class="btn">Subscribe</button>
  </section>
</main>

<footer class="abs site-footer">
  <div class="contact"><b>Phone:</b> 555- 014-2290, <b>Email:</b> info@bramblewickbids.com<br>Copyright (C) <b>BRAMBLEWICK</b> 2013 - 2014 .&nbsp; All Rights Reserved</div>
  <div class="foot-brand"><i></i><span>BRAMBLEWICK</span></div>
  <div class="badge-a"></div>
  <div class="badge-b"></div>
</footer>

</body>
</html>
```